Reed & Vale NC grand opening (for BILLBOARD)

Advertising the grand opening of our cannabis/hemp shop in NC. We will sell all things hemp (flower, cartridges, disposables, edibles, creams, lotions, pet products etc...)

Requirements
Must have
• include, open starting Aug 1, but grand opening Aug 15th.
Nice to have
• Difference slogan ideas "Save some cash, buy our grass" "Find your perfect high at Reed & Vale cannabis store" "Experience Nature's Gift: Reed & Vale Cannabis Store"

```html
<!DOCTYPE html>
<html lang="en">
<head>
<meta charset="utf-8">
<title>Reed &amp; Vale Grand Opening Billboard</title>
<link rel="stylesheet" href="https://fonts.googleapis.com/css2?family=Montserrat:wght@400;500;600;700;800;900&display=swap">
<style>
  :root {
    --canvas: #ffffff;
    --deep-green: #0b6a37;
    --dark-green: #064d27;
    --lime: #79c33b;
    --lime-bright: #8fd13f;
    --ink: #111111;
    --white: #ffffff;
    --sign-dark: #24272b;
    --stone: #9ea1a4;
  }
  * { box-sizing: border-box; margin: 0; padding: 0; }
  html, body { width: 1200px; height: 453px; overflow: hidden; background: var(--canvas); }
  body { font-family: "Montserrat", sans-serif; position: relative; }

  .billboard {
    position: absolute; left: 36px; top: 90px; width: 1128px; height: 332px; overflow: hidden;
  }
  .backdrop-photo {
    position: absolute; inset: 0;
    background:
      radial-gradient(ellipse 260px 180px at 560px 90px, #e9b640 0%, rgba(233,182,64,0) 70%),
      radial-gradient(ellipse 300px 220px at 200px 140px, #6f9a52 0%, rgba(111,154,82,0) 75%),
      linear-gradient(90deg, #2f5a2a 0%, #7b8f3c 30%, #c7a23a 48%, #a9c23b 62%, #8fd13f 80%, #7fcf38 100%);
  }
  .backdrop-shade {
    position: absolute; left: 0; right: 0; bottom: 0; height: 90px;
    background: linear-gradient(180deg, rgba(11,106,55,0) 0%, var(--deep-green) 100%);
  }

  .tag-grand {
    position: absolute; left: 56px; top: 52px; width: 274px; height: 35px;
    background: var(--lime); color: var(--ink);
    font-weight: 900; font-size: 27px; line-height: 35px; padding-left: 10px; letter-spacing: 0.3px;
    white-space: nowrap;
  }
  .tag-date {
    position: absolute; left: 323px; top: 67px; width: 186px; height: 34px;
    background: var(--lime); clip-path: polygon(0 0, 86% 0, 100% 100%, 0 100%);
    color: var(--ink); font-weight: 600; font-size: 22px; line-height: 36px; padding-left: 14px;
    white-space: nowrap;
  }

  .headline { position: absolute; left: 58px; top: 114px; color: var(--white); white-space: nowrap; }
  .headline .line-light {
    display: block; font-weight: 400; font-size: 40px; line-height: 44px; letter-spacing: -0.6px;
    -webkit-text-stroke: 1px #1b2a12; paint-order: stroke fill;
  }
  .headline .line-bold {
    display: block; font-weight: 800; font-size: 40px; line-height: 50px; letter-spacing: -0.6px;
    text-shadow: 2px 2px 0 var(--dark-green), -1px -1px 0 var(--dark-green), 1px -1px 0 var(--dark-green), -1px 1px 0 var(--dark-green);
  }
  .headline .line-bold:first-of-type { margin-top: 4px; }

  .open-badge {
    position: absolute; left: 481px; top: 131px; width: 168px; height: 101px;
    background: var(--white); border: 4px solid var(--lime); border-radius: 30px;
    box-shadow: 0 0 0 2px var(--deep-green);
    text-align: center; color: var(--deep-green); padding-top: 7px;
  }
  .open-badge .badge-strong { display: block; font-weight: 800; font-size: 26px; line-height: 28px; }
  .open-badge .badge-date { display: block; font-weight: 500; font-size: 23px; line-height: 25px; }

  .learn-more {
    position: absolute; left: 506px; top: 256px; width: 124px; height: 31px;
    display: flex; align-items: center;
    background: var(--lime); border-radius: 16px;
    text-decoration: none;
  }
  .learn-more-label {
    padding-left: 12px; color: var(--dark-green);
    font-weight: 800; font-size: 9.5px; letter-spacing: 0.3px; white-space: nowrap;
  }
  .learn-more-icon { position: absolute; right: 0; top: 0; width: 31px; height: 31px; }

  .storefront-illustration {
    position: absolute; left: 689px; top: 17px; width: 414px; height: 303px;
    background: linear-gradient(180deg, #5b6066 0%, var(--sign-dark) 12%, var(--sign-dark) 42%, var(--stone) 46%, #c9cbcd 100%);
  }
  .store-sign-name {
    position: absolute; left: 0; right: 0; top: 58px; text-align: center;
    color: var(--lime-bright); font-weight: 800; font-size: 36px;
  }
  .store-sign-address {
    position: absolute; left: 0; right: 0; top: 126px; height: 14px;
    background: var(--lime); text-align: center; color: var(--ink);
    font-weight: 600; font-size: 12.5px; line-height: 14px;
  }
</style>
</head>
<body>
  <section class="billboard">
    <div class="backdrop-photo" role="img" aria-label="Close-up photo of dewy cannabis leaves against a soft green and amber blur"></div>
    <div class="backdrop-shade"></div>

    <div class="tag-grand">GRAND OPENING</div>
    <div class="tag-date">15 AUGUST</div>

    <h1 class="headline">
      <span class="line-light">FIND YOUR</span>
      <span class="line-light">PERFECT HIGH AT</span>
      <span class="line-bold">REED &amp; VALE</span>
      <span class="line-bold">CANNABIS STORE</span>
    </h1>

    <div class="open-badge">
      <span class="badge-strong">OPEN</span>
      <span class="badge-strong">STARTING</span>
      <span class="badge-date">AUGUST 1</span>
    </div>

    <a class="learn-more" href="#">
      <span class="learn-more-label">LEARN MORE</span>
      <svg class="learn-more-icon" viewBox="0 0 31 31" aria-hidden="true">
        <circle cx="15.5" cy="15.5" r="15.5" fill="#0b6a37"/>
        <path d="M10 10l5.5 5.5L10 21M16 10l5.5 5.5L16 21" fill="none" stroke="#fff" stroke-width="2.6" stroke-linecap="round" stroke-linejoin="round"/>
      </svg>
    </a>

    <div class="storefront-illustration" role="img" aria-label="Illustrated cannabis shop storefront with display windows, glass door and a we're open sidewalk sign">
      <div class="store-sign-name">Reed &amp; Vale</div>
      <div class="store-sign-address">Exit 4B Millbrook Rd</div>
    </div>
  </section>
</body>
</html>
```